Tri-fold Brochure Design for Law Firm

I need a tri-fold brochure to give to prospective clients.
I have attached a Photoshop design file of a tri-fold brochure. The content (copy) is good, however, he brochure itself looks very amateurish.
I want a professional, sophisticated looking brochure.
The law firm specializes in commercial debt collection.
The law firm is located in New York City.
Our target market is business owners, doctors, lawyers, collection agencies and accountants.
Visit my website which is being designed at www.dorvenlaw.com. I like the font used for the name of my company and the rich blue color used.

Target Market(s)

Business Owners, Doctors, Law Firms and Accountants

Industry/Entity Type

Law Firm

Font styles to use
Serif

Requirements
Must have
• Professional quality graphic work. Attention to details.
• PHOTOGRAPHS ONLY, NO CLIP-ART.
• DARK COLORS - NAVY BLUE, HUNTER GREEN, BLACK, GRAY & WHITE
Nice to have
• I want it to look smart, modern and sophisticated.
• Visit my website which is being designed at www.dorvenlaw.com. I like the font used for the name of my company and the rich blue color used.
Should not have
• Bad artwork
• CLIP ART

```html
<!DOCTYPE html>
<html lang="en">
<head>
<meta charset="utf-8">
<title>Marcus Dorven &amp; Company PLLC — Tri-fold Brochure</title>
<link href="https://fonts.googleapis.com/css2?family=Libre+Bodoni:wght@400;500&family=Roboto+Condensed:wght@300;400&display=swap" rel="stylesheet">
<style>
:root{
  --navy:#14466a;
  --navy-deep:#0f3a5a;
  --charcoal:#262626;
  --ink:#2b2b2b;
  --muted:#555;
  --paper:#ffffff;
  --backdrop:#a6a6a6;
  --serif:"Libre Bodoni", "Bodoni Moda", Georgia, serif;
  --sans:"Roboto Condensed", "Arial Narrow", sans-serif;
}
*{box-sizing:border-box;margin:0;padding:0}
html,body{width:1200px;height:864px;overflow:hidden;background:var(--backdrop)}
.canvas{position:relative;width:1200px;height:864px}
.spread{position:absolute;top:209px;width:600px;height:464px;background:var(--paper);transform:scale(.96);transform-origin:0 0;overflow:hidden;font-family:var(--sans);color:var(--ink)}
.spread--outside{left:16px}
.spread--inside{left:608px}
.shapes{position:absolute;inset:0}
.block{position:absolute}
h2{font-family:var(--serif);font-weight:400;font-size:13px;color:var(--ink);margin-bottom:8px}
.inside-head{font-family:var(--serif);font-weight:400;font-size:9.5px;margin-bottom:6px}
p,li{font-size:5.2px;line-height:1.45}
p{margin-bottom:5px}
.lead{font-size:7px;margin:6px 0 14px}
.serve{display:grid;grid-template-columns:1fr 1fr;column-gap:10px;list-style:disc;padding-left:12px;margin-bottom:18px}
.serve li{margin-bottom:2.5px}
.sub{font-size:6.5px;text-transform:uppercase;color:var(--navy);margin:7px 0 5px;letter-spacing:.2px}
.on-dark{color:#fff}
.on-dark p,.on-dark li{color:#e8eef3}
.on-dark .sub{color:#fff}
.fee-list{list-style:disc;padding-left:12px;margin-bottom:7px}
.contact-card p{font-size:4.6px;line-height:1.5;margin-bottom:0;color:#ddd;white-space:nowrap}
.contact-card .gap{margin-top:7px}
.contact-card .address{padding-left:32px}
.contact-band{display:flex;align-items:center;gap:22px}
.contact-band .label{font-family:var(--serif);font-size:12px;color:#fff}
.contact-band p{font-size:5.3px;color:#fff;margin-bottom:4px}
.firm-title{font-family:var(--serif);font-size:14px;line-height:1.35;letter-spacing:.6px;color:var(--navy)}
.cover-foot p{font-size:5.4px;letter-spacing:1px;color:#fff;margin-bottom:2px}
.mark-name{font-family:var(--serif);font-size:10px;color:var(--navy);text-align:center;letter-spacing:1px}
.right-copy p{color:#333}
</style>
</head>
<body>
<main class="canvas">

  <section class="spread spread--outside" aria-label="Brochure outside">
    <svg class="shapes" viewBox="0 0 600 464" aria-hidden="true">
      <polygon points="0,0 263,0 263,26 85,70 0,42" fill="var(--navy)"/>
      <rect x="263" y="0" width="137" height="228" fill="var(--charcoal)"/>
      <circle cx="263" cy="138" r="46" fill="#fff" stroke="var(--navy)" stroke-width="2"/>
      <rect x="200" y="228" width="200" height="70" fill="var(--navy)"/>
      <defs>
        <linearGradient id="coverSky" x1="0" y1="0" x2="0.4" y2="1">
          <stop offset="0" stop-color="#2a7fa8"/>
          <stop offset="0.45" stop-color="#7cc6d6"/>
          <stop offset="1" stop-color="#c8e6e8"/>
        </linearGradient>
      </defs>
      <rect x="411" y="14" width="176" height="437" fill="url(#coverSky)" role="img" aria-label="Photograph of a smiling professional looking upward against a blue sky"/>
      <polygon points="400,232 587,290 587,312 400,254" fill="#e6f2f4" opacity=".75"/>
      <polygon points="400,254 587,312 587,318 400,260" fill="var(--navy)"/>
      <polygon points="411,300 587,336 587,451 411,451" fill="var(--navy)"/>
      <polygon points="400,228 411,232 411,268 400,264" fill="var(--navy)"/>
    </svg>

    <div class="block" style="left:14px;top:76px;width:170px">
      <h2>A trusted partner</h2>
      <p>We are in the business of debt collection. Our primary focus is to help our clients secure the payments they are owed. We work closely with both private clients and leading service professionals, such as attorneys and accountants, to provide added value to their clients through customized debt collection services.</p>
      <p class="lead">We value our relationships as trusted advisors.</p>
      <h2>We proudly serve...</h2>
      <ul class="serve">
        <li>Law firms</li><li>Doctors and Healthcare Professionals</li>
        <li>Accounting Firms</li><li>Carting Companies</li>
        <li>Manufacturers</li><li>Oil Companies</li>
        <li>Wholesalers and Distributors</li><li>Freight Forwarders &amp; Custom Brokers</li>
        <li>Collection Agencies</li><li>Publishing and Advertising Companies</li>
        <li>Financial Service Companies</li><li>Construction and Real Estate Firms</li>
        <li>Factors</li>
      </ul>
      <h2>Why use us</h2>
      <p>Anyone can sue a Debtor.</p>
      <p>It's not difficult to get nasty or to treat people who owe you money in a rude and unprofessional way. However, very few people have the skill, temperament and experience needed to effectively negotiate with Debtors, stakeholders, lawyers, as well as court personnel, sheriffs and bankers to efficiently collect the most money possible in the least amount of time. We truly understand the nature of commercial debt.</p>
      <p class="lead" style="font-size:6.5px">Collecting money is a specialized skill.</p>
    </div>

    <div class="block" style="left:223px;top:126px;width:80px">
      <p class="mark-name">DORVEN</p>
    </div>

    <div class="block contact-card" style="left:282px;top:60px;width:115px">
      <p>MARCUS J. DORVEN, ESQUIRE</p>
      <p>President</p>
      <p>mdorven@dorvenlaw.com</p>
      <p>(212) 555-0163 Cell</p>
      <div class="address">
        <p class="gap">Westchester County Office</p>
        <p>450 Hillcrest Avenue</p>
        <p>Suite 210, White Plains</p>
        <p>New York 10601</p>
        <p>(Off Exit 8 on I-287)</p>
        <p class="gap">Mailing address:</p>
        <p>310 Lexington Avenue</p>
        <p>Suite 5120</p>
        <p>New York, New York 10016</p>
      </div>
    </div>

    <div class="block contact-band" style="left:226px;top:238px;width:170px;height:50px">
      <span class="label">Contact us</span>
      <div>
        <p>Toll Free (877) 555-0142</p>
        <p>Local (212) 555-0186</p>
        <p>Fax (917) 555-0127</p>
      </div>
    </div>

    <div class="block" style="left:425px;top:56px;width:160px">
      <p class="firm-title">MARCUS DORVEN &amp;<br>COMPANY PLLC</p>
    </div>

    <div class="block cover-foot" style="left:423px;top:376px;width:160px">
      <p>DEBIT COLLECTION ATTORNEYS</p>
      <p>IN NEW YORK STATE</p>
      <p style="margin-top:30px">DorvenLaw.com</p>
      <p>(877) 555-0142</p>
    </div>
  </section>

  <section class="spread spread--inside" aria-label="Brochure inside">
    <svg class="shapes" viewBox="0 0 600 464" aria-hidden="true">
      <defs>
        <linearGradient id="teamPhoto" x1="0" y1="0" x2="1" y2="0">
          <stop offset="0" stop-color="#bdbdbd"/>
          <stop offset="0.5" stop-color="#e2e2e2"/>
          <stop offset="1" stop-color="#f2f2f2"/>
        </linearGradient>
        <linearGradient id="advisorPhoto" x1="0" y1="0" x2="1" y2="1">
          <stop offset="0" stop-color="#f0f0f0"/>
          <stop offset="0.6" stop-color="#e0e0e0"/>
          <stop offset="1" stop-color="#bcbcbc"/>
        </linearGradient>
      </defs>
      <rect x="0" y="0" width="200" height="168" fill="var(--navy)"/>
      <rect x="0" y="12" width="190" height="150" fill="url(#teamPhoto)" role="img" aria-label="Black and white photograph of two colleagues in profile"/>
      <rect x="247" y="0" width="153" height="464" fill="var(--navy)"/>
      <rect x="400" y="0" width="200" height="464" fill="url(#advisorPhoto)" role="img" aria-label="Soft black and white photograph of a professional woman in an office"/>
    </svg>

    <div class="block" style="left:14px;top:184px;width:160px">
      <h3 class="inside-head">Who we are</h3>
      <p>MARCUS DORVEN &amp; COMPANY, PLLC ("DORVEN") is a New York based law firm devoted to the collection of accounts receivable and business debts.</p>
      <p class="sub">What we do</p>
      <p>Within 24 to 72 hours of receiving a claim, we will verify the debt, investigate the Debtor, skip trace all known stakeholders and file a lawsuit with the intent of collecting the full amount due in the shortest time possible.</p>
      <p>We will use all legal means necessary to locate, identify, seize, or otherwise garnish a Debtor's assets and income, while always having an attorney available to speak directly with the Debtor to achieve an amicable resolution as quickly as possible.</p>
      <p class="sub">Our mission</p>
      <p>Our mission is to protect our clients' bottom line, while preserving their reputation.</p>
      <p>We recognize and appreciate that your Debtor was once a trusted customer and may be a source of future revenue.</p>
      <p>We treat all Debtors with respect, while aggressively seeking to collect all monies owed.</p>
    </div>

    <div class="block on-dark" style="left:262px;top:44px;width:124px">
      <h3 class="inside-head">Flexible fee structure</h3>
      <p>We recognize that each claim is unique, therefore to better serve our clients we offer a variety of fee structures that meet the needs of our clients.</p>
      <p>Including:</p>
      <ul class="fee-list">
        <li>Contingency Fee</li><li>Flat Fee</li><li>Hourly fee</li>
        <li>Monthly or Annual Retainer</li><li>Any combination of the above</li>
      </ul>
      <p class="sub">Handling medical receivables</p>
      <p>Medical receivables require a soft touch.</p>
      <p>Doctors and health organizations often write-off tens of thousands of dollars in unpaid deductibles and co-insurance which are rightfully due them out of fear that pursuing these debts will alienate, upset or offend their patients.</p>
      <p>We offer non-legal, HIPPA compliant collection methods which can effectively and consistently turn these otherwise uncollectible assets into real cash.</p>
      <p>Using a combination of letters and phone calls, our staff contacts patients in a professional and friendly manner to arrange for payments, as small as $15 per month, encouraging them to pay all monies owed.</p>
    </div>

    <div class="block right-copy" style="left:416px;top:44px;width:165px">
      <h3 class="inside-head">Credit advisory services</h3>
      <p>How well do you really know your customers?</p>
      <p>As an added service to all of our clients, we will draft a customized credit application to be distributed to all of their customers.</p>
      <p>Working closely and alongside their salespeople, we will discreetly review and verify the customers' information and investigate all known stakeholders in order to determine creditworthiness.</p>
      <p>As your credit advisor, we will then make a meaningful recommendation with regard to the amount and terms credit should be offered to specific customers.</p>
      <p>Once a credit determination is made, we can provide the client with a credit agreement detailing each parties' obligations. Using such agreements minimizes risk, while enhancing our clients' professional stature with their customers.</p>
      <p class="sub">Keeping you in compliance</p>
      <p>As your collection attorney and advisor, we will assure that your collection practices are in full compliance with all applicable Federal and State laws, including The Fair Debt Collection Practices Act (FDCPA) and The Health Insurance Portability and Accountability Act (HIPPA).</p>
      <p class="sub">State of the art technology</p>
      <p>Our firm prides itself on utilizing the state of the art technology in law office management, telephony, cyber security, document production, and cloud storage.</p>
      <p>Our clients can be assured that their critical business data is stored in a safe, secure, and confidential environment, while allowing us to seamlessly handle a large and ever growing book of business in a timely manner.</p>
    </div>
  </section>

</main>
</body>
</html>
```